Humor Novelist needs a warm, playful cover

I need a cover for my Lumora ebook and 5 x 8 paperback, Braver as Sasquatches: A Farce. It’s a humor novel set in America’s heartland about a guy fresh out of college who stumbles onto a town full of werewolves. It’s funny but not wacky—a paranormal coming of age story. Should be cheeky but not look like pie-in-the-face humor.

FRONT COVER should include:

Braver as Sasquatches: A Farce
Dominic Pellworth

BACK COVER should include:

Dominic Pellworth

Fresh out of college and armed with a research grant, Milo Vantrask heads to the backwoods of his home state to look for Bigfoot. While camping near his grandfather’s vineyard he learns that the forest is populated by wolves—unusually clever ones. He discovers a nearby town where malt shops, milkmen, and the 1950’s never stopped. Along with his lecherous grandfather and mysterious girlfriend, Saul must navigate wolfmen and gun-toting rednecks to discover the secret uniting an entire town to werewolves.

“Probably the funniest paranormal coming of age novel to come out since that awful paperback about shiny vampires with mood swings.”
– The Meridian Trumpet

“None of the awkward sex scenes in this book indicate that Dominic Pellworth has ever actually had sex. I liked the stuff about werewolves, though.”
– The Hollowmere Ledger

“Reads like Beaumont Trelawny retelling something Morton Quayle cranked out before he sobered up.”
– Galloway Critiques

Target Market(s)

Adult comedy readers

Industry/Entity Type

Book Publisher

Font styles to use
Serif

Colors
0292cd
33a6d7
85cae6
86cfc6
33b8a4
00a990
0255a3
3276b5
85abd2

Requirements
Must have
• (on the front) Author Name, Title (on the back) Synopsis and reviews
Should not have
• A horror feel to it, romance cover feel to it

```html
<!DOCTYPE html>
<html lang="en">
<head>
<meta charset="utf-8">
<title>Braver as Sasquatches: A Farce — Dominic Pellworth</title>
<link href="https://fonts.googleapis.com/css2?family=Playfair+Display:wght@700;900&family=Great+Vibes&family=Crimson+Text:wght@400&display=swap" rel="stylesheet">
<style>
  :root {
    --page-bg: #ececec;
    --forest-top: #5f9fa8;
    --forest-mid: #2f4f55;
    --figure-dark: #1f2326;
    --forest-floor: #3d5440;
    --title-white: #ffffff;
    --title-shadow: rgba(0, 0, 0, 0.75);
    --band-red: #a5141f;
    --band-red-light: #cf4a55;
    --band-rule: #f4f4f4;
  }
  * { margin: 0; padding: 0; box-sizing: border-box; }
  html, body {
    width: 1200px;
    height: 900px;
    overflow: hidden;
    background: var(--page-bg);
  }
  .canvas {
    position: relative;
    width: 1200px;
    height: 900px;
  }
  .front-cover {
    position: absolute;
    left: 340px;
    top: 34px;
    width: 520px;
    height: 832px;
    overflow: hidden;
    box-shadow: 0 6px 18px rgba(0,0,0,0.25);
  }
  .cover-art {
    position: absolute;
    inset: 0;
    background:
      radial-gradient(ellipse 42% 60% at 60% 55%, var(--figure-dark) 0%, rgba(31,35,38,0.85) 45%, rgba(31,35,38,0) 75%),
      radial-gradient(ellipse 60% 35% at 15% 85%, rgba(200,210,210,0.45) 0%, rgba(200,210,210,0) 70%),
      linear-gradient(180deg, var(--forest-top) 0%, var(--forest-mid) 40%, var(--forest-floor) 80%, #2c3a2e 100%);
  }
  .title {
    position: absolute;
    left: 0;
    top: 0;
    width: 100%;
    height: 100%;
    color: var(--title-white);
    text-shadow: 2px 3px 4px var(--title-shadow);
  }
  .title-word {
    position: absolute;
    font-family: "Playfair Display", serif;
    font-weight: 900;
    line-height: 1;
    transform-origin: left top;
    transform: scaleX(0.78);
    white-space: nowrap;
  }
  .title-word--first { left: 22px; top: 70px; font-size: 92px; }
  .title-word--last { left: 40px; top: 300px; font-size: 88px; }
  .title-joiner {
    position: absolute;
    left: 110px;
    top: 150px;
    font-family: "Great Vibes", cursive;
    font-size: 150px;
    line-height: 1;
  }
  .subtitle {
    position: absolute;
    right: 50px;
    top: 470px;
    font-family: "Great Vibes", cursive;
    font-size: 64px;
    color: var(--title-white);
    text-shadow: 1px 2px 3px var(--title-shadow);
  }
  .author-band {
    position: absolute;
    left: 0;
    bottom: 0;
    width: 100%;
    height: 128px;
    border-top: 3px solid var(--band-rule);
    background: linear-gradient(90deg, var(--band-red-light) 0%, var(--band-red) 35%, var(--band-red) 100%);
    display: flex;
    align-items: center;
    justify-content: center;
  }
  .author-name {
    font-family: "Crimson Text", serif;
    font-weight: 400;
    font-size: 46px;
    color: var(--title-white);
    letter-spacing: 0.5px;
  }
</style>
</head>
<body>
  <main class="canvas">
    <section class="front-cover">
      <div class="cover-art" role="img" aria-label="Photograph of a young man in a black hat, tinted glasses and dark waistcoat holding a rifle across his shoulders in a misty blue-green forest"></div>
      <h1 class="title">
        <span class="title-word title-word--first">Braver</span>
        <span class="title-joiner">as</span>
        <span class="title-word title-word--last">Sasquatches:</span>
      </h1>
      <p class="subtitle">A Farce</p>
      <footer class="author-band">
        <p class="author-name">Dominic Pellworth</p>
      </footer>
    </section>
  </main>
</body>
</html>
```